Los Angeles based Demolition, Grading, and Structural concrete Contractor in need of a Sale brochure

We are a Los Angeles-based demolition, grading, and structural concrete contractor looking for a professionally designed sales brochure that represents our company and services. The brochure should be visually appealing, easy to read, and include the following:

-Company Logo: Prominently displayed to enhance brand identity.

-Services We Offer: A clear breakdown of our key services, including demolition, grading, and structural concrete work.

-Project Scope & Capabilities: A brief explanation of the type of projects we handle (residential, commercial, industrial).

-Pricing Information: Mention that demolition services start at $20,000. This price includes complete demolition of structure, safe debris removal and hauling, site preparation for new construction.

-Contact Information: Our phone number(555.206.1187), email(contact@bravoridgebuilders.example) , and website for potential clients to reach out.

The design should reflect the professionalism and strength of our industry, using a modern, clean layout with bold colors that align with construction and demolition themes. Images of past work or stock photos representing our services are encouraged.

Final deliverables should be print-ready (PDF) and digital-friendly formats. Looking forward to creative and impactful designs!

```html
<!DOCTYPE html>
<html lang="en">
<head>
<meta charset="utf-8">
<title>Bravo Ridge Builders – Sales Brochure</title>
<link href="https://fonts.googleapis.com/css2?family=Montserrat:wght@400;500;600;700;800&family=Oswald:wght@300;500&display=swap" rel="stylesheet">
<style>
:root{
  --blue:#1f74bd;
  --blue-light:#5fb2f2;
  --black:#050505;
  --white:#ffffff;
  --grey:#b9b9b9;
  --grey-dark:#5d5d5d;
  --tab:#7a7a7a;
  --text:#222;
  --sand:#c9a57a;
  --sky:#e9b877;
}
*{margin:0;padding:0;box-sizing:border-box}
html,body{width:1200px;height:2400px;overflow:hidden}
body{background:var(--grey);font-family:'Montserrat',sans-serif;color:var(--text);position:relative}
.spread{position:absolute;left:20px;width:1160px;height:750px;background:var(--white);overflow:hidden;box-shadow:0 10px 24px rgba(0,0,0,.28)}
.spread--outer{top:370px}
.spread--inner{top:1250px}
.abs{position:absolute}
.photo{position:absolute}
.brand{position:absolute;text-align:center;font-weight:800;color:var(--blue);letter-spacing:1px;line-height:1.05}
.brand small{display:block;font-weight:800;font-size:.42em;letter-spacing:.55em;margin-top:4px}

/* outer spread */
.outer-band{left:0;top:456px;width:1160px;height:294px;background:var(--blue)}
.frame-back{left:95px;top:175px;width:392px;height:248px;background:var(--black)}
.frame-back .photo{left:12px;top:12px;width:368px;height:224px;background:linear-gradient(135deg,#bfa78a,#8d7a63 50%,#c8b59a);border:3px solid var(--white)}
.contact-title{left:0;width:580px;top:478px;text-align:center;color:var(--white);letter-spacing:3px;font-size:21px;line-height:1.05}
.contact-title b{font-weight:800}
.contact-icons{left:150px;top:538px;width:280px;height:36px}
.contact-lines{left:0;width:580px;top:588px;text-align:center;color:var(--white);font-size:14px;line-height:1.3}
.contact-lines p{margin-bottom:18px}
.frame-front{left:623px;top:160px;width:484px;height:300px;background:var(--black)}
.frame-front-white{left:638px;top:175px;width:453px;height:315px;background:var(--white);box-shadow:0 6px 10px rgba(0,0,0,.25)}
.frame-front-white .photo{left:12px;top:12px;width:429px;height:291px;background:linear-gradient(180deg,var(--sky) 0%,#caa37b 30%,var(--sand) 55%,#b58f63 100%)}
.cover-head{left:580px;width:580px;top:510px;text-align:center;color:var(--white)}
.cover-head .kicker{font-size:24px;letter-spacing:2px;font-weight:500}
.cover-head .big{font-size:36px;font-weight:800;color:var(--blue-light);line-height:1;margin-top:2px;letter-spacing:.5px}
.pill-dark{display:inline-block;background:var(--black);color:var(--white);border-radius:6px;font-size:17px;letter-spacing:2px;padding:3px 10px;margin-top:8px;font-weight:500}
.cover-tag{font-size:10px;margin-top:10px;line-height:1.25}
.cover-web{font-size:13px;letter-spacing:3px;margin-top:34px}

/* inner spread */
.band-left{left:0;top:0;width:350px;height:750px;background:var(--blue)}
.band-top{left:0;top:0;width:580px;height:190px;background:var(--blue)}
.band-right{left:965px;top:0;width:195px;height:160px;background:var(--blue)}
.about{left:37px;top:40px;width:515px;height:145px;background:var(--black);border:2px solid var(--white);color:var(--white)}
.about .photo{left:13px;top:13px;width:152px;height:117px;background:linear-gradient(180deg,#8fb5da 0%,#cfd8de 40%,#b29876 100%);border:1px solid #fff}
.about h3{position:absolute;left:178px;top:14px;font-size:14px;color:var(--blue-light);font-weight:800}
.about p{position:absolute;left:178px;top:36px;width:322px;font-size:8.2px;line-height:1.3}
.sec-head{left:40px;top:200px;display:flex;align-items:center;gap:10px;color:var(--black);font-weight:800;font-size:15px}
.svc{left:38px;width:265px;color:var(--white)}
.svc h4{font-size:14px;font-weight:800;margin-bottom:6px}
.svc p{font-size:8.2px;line-height:1.3}
.svc-rule{left:38px;width:270px;height:1px;background:rgba(255,255,255,.5)}
.svc-photo{left:318px;width:234px;height:130px;background:var(--white);box-shadow:0 4px 8px rgba(0,0,0,.25)}
.svc-photo .photo{left:6px;top:6px;width:222px;height:118px}
.foot{top:700px;height:14px}
.foot .pill{position:absolute;left:0;top:0;background:var(--black);color:var(--white);font-size:8px;border-radius:8px;padding:2px 10px;line-height:10px}
.foot .rule{position:absolute;top:7px;height:1px;background:var(--black)}
.foot .dot{position:absolute;top:2px;width:10px;height:10px;border-radius:50%;background:var(--black)}

.col-mid{left:607px;width:192px}
.col-mid h3{font-size:14px;font-weight:800;color:var(--grey-dark);line-height:1}
.col-mid p{font-size:7.4px;line-height:1.26}
.col-mid h3.blue{color:var(--blue)}
.price-line{left:607px;top:385px;width:200px;border-top:1px dashed var(--grey-dark)}
.price-amount{font-family:'Oswald',sans-serif;font-weight:300;font-size:20px;color:var(--black);margin-top:2px;white-space:nowrap}
.price-amount span{font-weight:500;color:var(--blue);font-size:32px}
.price-amount sup{font-size:16px}
.price-items{left:607px;top:545px;width:195px}
.price-items .item{display:flex;align-items:center;gap:10px;font-size:8.6px;font-weight:600;padding:6px 0;border-bottom:1px solid #bbb;height:43px}
.price-items .item:last-child{border:0}

.projects{left:830px;top:43px;width:288px;height:630px;background:var(--black);color:var(--white)}
.projects h2{position:absolute;left:22px;top:14px;font-size:16px;line-height:1.05;font-weight:800;color:var(--blue-light)}
.projects h2 span{font-weight:400;color:var(--white)}
.proj{position:absolute;left:0;width:288px}
.proj .tab{position:absolute;left:-12px;top:-4px;width:50px;height:30px;background:var(--tab);border-radius:0 15px 15px 0}
.proj .tab i{position:absolute;right:3px;top:3px;width:24px;height:24px;border-radius:50%;background:var(--white);border:2px solid var(--blue)}
.proj h4{position:absolute;left:50px;top:5px;font-size:11px;font-weight:600;white-space:nowrap}
.proj h4 b{color:var(--blue-light);font-weight:700}
.proj .photo{left:50px;top:28px;width:200px;height:82px;border:2px solid var(--white)}
.proj p{position:absolute;left:50px;top:116px;width:210px;font-size:7.6px;line-height:1.25}
</style>
</head>
<body>

<section class="spread spread--outer">
  <div class="abs outer-band"></div>

  <div class="brand" style="left:130px;top:90px;width:300px;font-size:30px">BRAVO RIDGE<small>BUILDERS</small></div>
  <div class="abs frame-back">
    <div class="photo" role="img" aria-label="Aerial view of concrete foundation formwork and rebar on a sandy site"></div>
  </div>

  <div class="abs contact-title">CONTACT US FOR<br><b>MORE INFORMATION</b></div>
  <svg class="abs contact-icons" viewBox="0 0 280 36">
    <g stroke="#fff" stroke-width="1.2"><line x1="0" y1="14" x2="50" y2="14"/><line x1="10" y1="18" x2="50" y2="18"/><line x1="0" y1="22" x2="50" y2="22"/>
    <line x1="230" y1="14" x2="280" y2="14"/><line x1="230" y1="18" x2="270" y2="18"/><line x1="230" y1="22" x2="280" y2="22"/></g>
    <g fill="#fff" stroke="#000" stroke-width="1.6">
      <circle cx="72" cy="18" r="14"/><circle cx="117" cy="18" r="14"/><circle cx="162" cy="18" r="14"/><circle cx="207" cy="18" r="14"/>
    </g>
    <path d="M66 11c1-1 3-1 3 0l1 3c0 1-1 2-1 2 1 2 2 3 4 4 0 0 1-1 2-1l3 1c1 0 1 2 0 3-3 3-13-7-12-12z" fill="#000"/>
    <path d="M117 27c-5-6-6-9-6-11a6 6 0 0 1 12 0c0 2-1 5-6 11z" fill="#000"/><circle cx="117" cy="16" r="2.2" fill="#fff"/>
    <rect x="154" y="12" width="16" height="12" rx="1" fill="#000"/><path d="M154 13l8 6 8-6" stroke="#fff" stroke-width="1.2" fill="none"/>
    <g stroke="#000" stroke-width="1.5" fill="none"><circle cx="207" cy="18" r="7.5"/><ellipse cx="207" cy="18" rx="3.2" ry="7.5"/><line x1="199.5" y1="18" x2="214.5" y2="18"/></g>
  </svg>
  <div class="abs contact-lines">
    <p>555.206.1187</p>
    <p>Lorem ipsum dolor sit<br>amet, consectetur</p>
    <p>contact@bravoridgebuilders.example</p>
    <p>www.bravoridgebuilders.example</p>
  </div>

  <div class="brand" style="left:740px;top:40px;width:280px;font-size:34px">BRAVO RIDGE<small>BUILDERS</small></div>
  <div class="abs frame-front"></div>
  <div class="abs frame-front-white">
    <div class="photo" role="img" aria-label="Excavator grading a hillside lot at sunset above the city"></div>
  </div>
  <div class="abs cover-head">
    <div class="kicker">LOS ANGELES BASED</div>
    <div class="big">DEMOLITION GRADING<br>&amp; STRUCTURAL CONCRETE</div>
    <div class="pill-dark">CONTRACTOR SERVICES</div>
    <div class="cover-tag">Committed to excellence, we leverage cutting-edge technology and skilled craftsmanship to<br>ensure the structural integrity and aesthetic appeal of every project we undertake.</div>
    <div class="cover-web">www.<b>bravoridgebuilders</b>.example</div>
  </div>
</section>

<section class="spread spread--inner">
  <div class="abs band-left"></div>
  <div class="abs band-top"></div>
  <div class="abs band-right"></div>

  <div class="abs about">
    <div class="photo" role="img" aria-label="Red excavator beside a concrete retaining wall on a hillside site"></div>
    <h3>ABOUT US</h3>
    <p>Bravo Ridge Builders is rooted in a deep understanding of the unique challenges presented by hillside properties, allowing us to deliver safe, efficient, and innovative solutions that meet the highest industry standards. Committed to excellence, we leverage cutting-edge technology and skilled craftsmanship to ensure the structural integrity and aesthetic appeal of every project we undertake. Our dedication to quality and customer satisfaction has established Bravo Ridge Builders as a trusted partner in the dynamic landscape of residential construction in Southern California.</p>
  </div>

  <div class="abs sec-head">
    <svg width="30" height="28" viewBox="0 0 30 28"><g fill="none" stroke="#fff" stroke-width="1.8"><circle cx="17" cy="9" r="5"/><path d="M17 1v3M17 14v3M9 9h3M22 9h3"/><path d="M2 22h6l5 3h9l6-5"/></g></svg>
    SERVICES WE OFFER
  </div>

  <div class="abs svc" style="top:245px">
    <h4>DEMOLITION</h4>
    <p>At Bravo Ridge Builders, our demolition services are designed to ensure the efficient and safe removal of structures while minimizing impact on the surrounding environment. We utilize advanced equipment and techniques to handle projects of any size, from residential buildings to large commercial sites. Our team of skilled professionals is trained to assess each project carefully, implementing effective strategies that prioritize safety and regulatory compliance.</p>
  </div>
  <div class="abs svc-rule" style="top:372px"></div>
  <div class="abs svc" style="top:395px">
    <h4>GRADING</h4>
    <p>Bravo Ridge Builders specializes in comprehensive site grading and mass excavation and hauling services, ensuring that each project lays a solid foundation for future development. Our skilled team utilizes state-of-the-art equipment to effectively manage soil removal, leveling, and site preparation, significantly enhancing the efficiency of construction timelines. We prioritize precision and safety throughout the process, adhering to industry standards while minimizing environmental impact.</p>
  </div>
  <div class="abs svc-rule" style="top:530px"></div>
  <div class="abs svc" style="top:567px">
    <h4>STRUCTURAL CONCRETE</h4>
    <p>Our structural concrete and foundation division offers comprehensive solutions tailored to meet the diverse needs of our clients. We specialize in everything from slab-on-grade foundations to shoring and retaining walls, as well as hillside basements. Our dedicated team employs advanced techniques and high-quality materials to ensure stability, durability, and safety for all types of projects.</p>
  </div>

  <div class="abs svc-photo" style="top:233px"><div class="photo" role="img" aria-label="Excavator clearing trees and debris on a wooded lot" style="background:linear-gradient(135deg,#6d7a4a,#b89a58 50%,#7d8060)"></div></div>
  <div class="abs svc-photo" style="top:386px"><div class="photo" role="img" aria-label="Graded hillside pad beside a tall concrete retaining wall" style="background:linear-gradient(180deg,#7fb0e0 0%,#9a9a92 40%,#c9a874 100%)"></div></div>
  <div class="abs svc-photo" style="top:540px"><div class="photo" role="img" aria-label="Structural concrete foundation under construction on a hillside" style="background:linear-gradient(180deg,#8ab3da 0%,#b7b2a6 45%,#9c8c75 100%)"></div></div>

  <div class="abs foot" style="left:38px;width:512px">
    <span class="pill">www.bravoridgebuilders.example</span>
    <span class="rule" style="left:150px;width:352px"></span><span class="dot" style="left:502px"></span>
  </div>

  <div class="abs col-mid" style="top:40px">
    <div style="display:flex;gap:8px;align-items:center">
      <svg width="28" height="30" viewBox="0 0 30 30"><g fill="none" stroke="#000" stroke-width="1.8"><circle cx="15" cy="8" r="5"/><path d="M15 13v8M9 28l6-7 6 7M5 17h20"/></g><circle cx="22" cy="6" r="3" fill="#1f74bd"/></svg>
      <h3>PROJECT SCOPE<br>&amp; CAPABILITIES</h3>
    </div>
    <p style="margin-top:6px">Bravo Ridge Builders is a leading construction firm established in 2019, driven by a commitment to excellence and innovation in the building industry. With a team of seasoned professionals, we specialize in delivering high-quality residential and commercial projects tailored to meet our clients' specific needs.</p>
    <h3 class="blue" style="margin-top:12px">OUR MISSION</h3>
    <p style="margin-top:6px">Centers on building lasting relationships with our clients, ensuring open communication and collaboration throughout each phase of the construction process. We prioritize safety, sustainability, and efficiency, employing the latest industry practices and technologies to enhance project outcomes.</p>
    <p style="margin-top:8px"><b>At Bravo Ridge Builders, we take pride in our ability to transform visions into reality,</b> providing not just structures but spaces that inspire and endure. Our diverse portfolio showcases our versatility and dedication to quality craftsmanship, making us a trusted partner in the construction landscape.</p>
  </div>

  <div class="abs price-line"></div>
  <div class="abs col-mid" style="top:400px">
    <div style="display:flex;gap:8px;align-items:center">
      <svg width="28" height="30" viewBox="0 0 28 30"><circle cx="17" cy="8" r="7" fill="#1f74bd"/><path d="M3 16h5v12H3zM9 17l5-5c1-1 3 0 2 2l-1 3h7c2 0 2 3 0 3 1 1 1 3-1 3 1 1 0 3-1 3H9z" fill="#000"/></svg>
      <h3>PRICING<br>INFORMATION</h3>
    </div>
    <div style="font-size:13px;font-weight:700;margin-top:12px">Demolition Services</div>
    <div class="price-amount">START AT <span><sup>$</sup>20,000</span></div>
    <div style="display:inline-block;background:#8a8a8a;color:#fff;font-size:8.6px;border-radius:5px;padding:2px 8px;margin-top:2px">THIS PRICE INCLUDES</div>
  </div>
  <div class="abs price-items">
    <div class="item"><svg width="24" height="24" viewBox="0 0 24 24"><path d="M2 20h20M4 20v-5h8v5M12 15l5-8 3 2M17 7l-3 4" stroke="#000" stroke-width="1.8" fill="none"/><circle cx="20" cy="10" r="2" fill="#1f74bd"/></svg>Complete demolition of<br>structure</div>
    <div class="item"><svg width="24" height="24" viewBox="0 0 24 24"><rect x="2" y="9" width="13" height="8" fill="none" stroke="#000" stroke-width="1.8"/><path d="M15 12h4l3 3v2h-7" fill="none" stroke="#000" stroke-width="1.8"/><circle cx="6" cy="19" r="2" fill="#1f74bd"/><circle cx="18" cy="19" r="2" fill="#1f74bd"/></svg>Safe debris removal &amp;<br>hauling</div>
    <div class="item"><svg width="24" height="24" viewBox="0 0 24 24"><path d="M12 14c-4-5-5-7-5-9a5 5 0 0 1 10 0c0 2-1 4-5 9z" fill="#1f74bd"/><path d="M3 22l4-6h10l4 6z" fill="none" stroke="#000" stroke-width="1.8"/></svg>Site preparation for new<br>construction.</div>
  </div>

  <div class="abs projects">
    <h2>THE TYPE OF PROJECTS<br><span>WE HANDLE</span></h2>
    <div class="proj" style="top:72px">
      <div class="tab"><i></i></div>
      <h4><b>RESIDENTIAL</b> PROJECTS</h4>
      <div class="photo" role="img" aria-label="Modern residential home with pool terrace" style="background:linear-gradient(180deg,#9cc4ea 0%,#dfe6ec 50%,#8b8f8a 100%)"></div>
      <p>Lorem ipsum dolor sit amet, consectetur adipiscing elit, sed do eiusmod tempor incididunt ut labore et dolore magna aliqua. Quis ipsum suspendisse ultrices gravida. Risus commodo viverra maecenas accumsan lacus vel facilisis.</p>
    </div>
    <div class="proj" style="top:255px">
      <div class="tab"><i></i></div>
      <h4><b>COMMERCIAL</b> PROJECTS</h4>
      <div class="photo" role="img" aria-label="Bright modern commercial office interior" style="background:linear-gradient(135deg,#e9f1f8,#b7cbe0 50%,#f4f4f4)"></div>
      <p>Lorem ipsum dolor sit amet, consectetur adipiscing elit, sed do eiusmod tempor incididunt ut labore et dolore magna aliqua. Quis ipsum suspendisse ultrices gravida. Risus commodo viverra maecenas accumsan lacus vel facilisis.</p>
    </div>
    <div class="proj" style="top:440px">
      <div class="tab"><i></i></div>
      <h4><b>INDUSTRIAL</b> PROJECTS</h4>
      <div class="photo" role="img" aria-label="Glass-walled industrial facility with sunlight" style="background:linear-gradient(135deg,#2d4f8f,#8fb2de 55%,#f2e6d2)"></div>
      <p>Lorem ipsum dolor sit amet, consectetur adipiscing elit, sed do eiusmod tempor incididunt ut labore et dolore magna aliqua. Quis ipsum suspendisse ultrices gravida. Risus commodo viverra maecenas accumsan lacus vel facilisis.</p>
    </div>
  </div>

  <div class="abs foot" style="left:607px;width:513px">
    <span class="pill">www.bravoridgebuilders.example</span>
    <span class="rule" style="left:150px;width:353px"></span><span class="dot" style="left:503px"></span>
  </div>
</section>

</body>
</html>
```